Postcard with promo code

We'd like to get a postcard designed to send to our customers with promotional offers. The postcard should have our logo incorporated along with some nice graphics of our products.

The promo card should have the following:
-Placeholder for offering like '$20 Off $50 or more total order'.
-Placeholder for promo code
-Placeholder for time limit.
-Incorporate some graphics of our products (see attached)
-Logo

You can use any number of the graphics attached for the design.

Reference to our website:
Website: www.plumvexa.com
Email: info@plumvexa.com
Phone: 281-473-9025

Need to have the design files Illustrator (AI) and Photoshop (PSD) formats.

Industry/Entity Type

Promo

Requirements
Must have
• The promo card should have the following:
• -Placeholder for offering like '$20 Off $50 or more total order'.
• -Placeholder for promo code
• -Placeholder for time limit.
• -Incorporate some graphics of our products (see attached)
• -Logo

```html
<!DOCTYPE html>
<html lang="en">
<head>
<meta charset="utf-8">
<title>Plum Vexa Promo Postcard</title>
<link rel="stylesheet" href="https://fonts.googleapis.com/css2?family=Marcellus&family=Crimson+Pro:wght@400;600;700&display=swap">
<style>
  :root {
    --page: #ffffff;
    --charcoal: #4a4a4a;
    --cream: #e6dfcf;
    --taupe: #c8bfae;
    --coupon-text: #8b8580;
    --coupon-dark: #4d4b49;
    --coupon-border: #6d6a66;
    --ribbon: #f04a4f;
    --linen-light: #f2efea;
    --linen-mid: #e3ded6;
    --white: #ffffff;
  }
  * { box-sizing: border-box; margin: 0; padding: 0; }
  html, body { width: 907px; height: 1200px; overflow: hidden; background: var(--page); }
  body { position: relative; font-family: "Crimson Pro", Georgia, serif; }

  .card {
    position: absolute; left: 33px; width: 839px; overflow: hidden;
    background: var(--white);
    box-shadow: 0 3px 10px rgba(0,0,0,0.35);
  }
  .card--front { top: 35px; height: 560px; }
  .card--back { top: 607px; height: 561px; }

  /* Front */
  .product-scene {
    position: absolute; left: 0; top: 0; width: 100%; height: 368px;
    background:
      radial-gradient(ellipse 90px 120px at 480px 140px, rgba(120,80,150,0.25), transparent 70%),
      radial-gradient(ellipse 110px 130px at 720px 170px, rgba(190,150,100,0.35), transparent 70%),
      linear-gradient(135deg, var(--linen-light), var(--linen-mid));
  }
  .ribbon {
    position: absolute; left: -42px; top: 30px; width: 190px; height: 30px;
    background: var(--ribbon); color: var(--white);
    transform: rotate(-45deg);
    font-weight: 700; font-size: 16px;
    letter-spacing: 0.5px; text-align: center; line-height: 30px;
  }
  .coupon {
    position: absolute; left: 80px; top: 111px; width: 219px; height: 217px;
    border: 2px dashed var(--coupon-border); border-radius: 24px;
    background: rgba(235,232,228,0.75);
    text-align: center; color: var(--coupon-text);
  }
  .coupon__amount { margin-top: 8px; font-size: 48px; line-height: 1; }
  .coupon__amount span { font-size: 34px; }
  .coupon__terms { margin-top: 8px; font-size: 19px; font-weight: 600; line-height: 1.35; }
  .coupon__code { margin-top: 14px; font-size: 19px; font-weight: 700; color: var(--coupon-dark); }
  .coupon__code span { color: var(--coupon-text); font-weight: 600; }
  .coupon__note { font-size: 15px; font-weight: 700; color: var(--coupon-dark); line-height: 1.4; }
  .coupon__note span { font-weight: 600; color: var(--coupon-text); }

  .brand-band {
    position: absolute; left: 0; top: 368px; width: 100%; height: 192px;
    background: var(--charcoal);
  }
  .brand-name {
    position: absolute; color: var(--cream);
    font-family: "Marcellus", Georgia, serif; text-align: center; white-space: nowrap;
  }
  .brand-name--front { left: 30px; top: 102px; width: 320px; font-size: 46px; letter-spacing: 1px; }

  .contact { position: absolute; left: 420px; top: 40px; color: var(--white); font-weight: 700; }
  .contact__row { display: flex; align-items: center; height: 40px; }
  .contact__row svg { flex: none; }
  .contact__web { font-size: 27px; margin-left: 12px; }
  .contact__mail { font-size: 23px; margin-left: 12px; }
  .contact__phone { font-size: 29px; margin-left: 16px; }
  .icon-mail { margin-left: 16px; }
  .icon-phone { margin-left: 30px; }

  /* Back */
  .gallery { position: absolute; left: 14px; top: 14px; width: 106px; }
  .gallery__item { width: 96px; height: 88px; margin: 0 auto 12px; border-radius: 40%; }
  .item-earrings-amethyst { background: radial-gradient(circle, #7b5a7a, #a08a6a 60%, #fff 75%); }
  .item-ring-citrine { background: radial-gradient(circle, #e8c34a, #8a8aa0 55%, #fff 72%); }
  .item-earrings-ruby { background: radial-gradient(circle, #c0242c, #a9a7a4 50%, #fff 72%); }
  .item-ring-sapphire { background: radial-gradient(circle, #23307a, #5a6aa0 55%, #fff 74%); }
  .item-ring-emerald { background: radial-gradient(circle, #1f8a5a, #c07090 50%, #fff 72%); }

  .story {
    position: absolute; left: 120px; top: 25px; width: 262px; height: 487px;
    background: var(--charcoal);
    clip-path: polygon(0 0, 100% 0, 81% 100%, 0 100%);
    padding: 0 14px 0 15px;
  }
  .brand-name--back { left: 0; top: 62px; width: 215px; font-size: 30px; letter-spacing: 0.5px; }
  .story__title {
    margin-top: 118px; color: var(--taupe); font-size: 15px; font-weight: 700;
    line-height: 1.4; letter-spacing: 0.3px;
  }
  .story__text {
    margin-top: 16px; width: 192px; color: var(--taupe); font-size: 15px; font-weight: 600;
    line-height: 22px;
  }
  .story__web {
    position: absolute; left: 8px; top: 412px; color: var(--white);
    font-size: 19px; font-weight: 700;
  }
</style>
</head>
<body>

  <section class="card card--front">
    <div class="product-scene" role="img" aria-label="Silver amethyst drop earrings, pendant necklace and ring on textured linen with a dried seed pod"></div>
    <div class="ribbon">SPECIAL OFFER</div>

    <div class="coupon">
      <p class="coupon__amount">$50 <span>OFF</span></p>
      <p class="coupon__terms">any order of<br>$250 or more</p>
      <p class="coupon__code">Promo code <span>PLUM50</span></p>
      <p class="coupon__note">Use at checkout<br>Good until <span>12.31.2016</span></p>
    </div>

    <div class="brand-band">
      <div class="brand-name brand-name--front">PLUM VEXA</div>

      <div class="contact">
        <div class="contact__row">
          <svg width="14" height="20" viewBox="0 0 14 20"><path d="M7 0a7 7 0 0 0-7 7c0 5 7 13 7 13s7-8 7-13a7 7 0 0 0-7-7z" fill="#fff"/><circle cx="7" cy="7" r="2.5" fill="#4a4a4a"/></svg>
          <span class="contact__web">WWW.PLUMVEXA.COM</span>
        </div>
        <div class="contact__row">
          <svg class="icon-mail" width="20" height="14" viewBox="0 0 20 14"><rect x="1" y="1" width="18" height="12" fill="none" stroke="#fff" stroke-width="1.6"/><path d="M1 1l9 7 9-7" fill="none" stroke="#fff" stroke-width="1.6"/></svg>
          <span class="contact__mail">info@plumvexa.com</span>
        </div>
        <div class="contact__row">
          <svg class="icon-phone" width="22" height="22" viewBox="0 0 22 22"><circle cx="11" cy="11" r="10" fill="none" stroke="#fff" stroke-width="1.4"/><path d="M8 6c-1 2 0 6 4 9l2-2-2-2-1 1c-1-1-2-3-2-4l1-1-1-2z" fill="#fff"/></svg>
          <span class="contact__phone">281-473-9025</span>
        </div>
      </div>
    </div>
  </section>

  <section class="card card--back">
    <div class="gallery">
      <div class="gallery__item item-earrings-amethyst" role="img" aria-label="Ottoman-style earrings with purple stones"></div>
      <div class="gallery__item item-ring-citrine" role="img" aria-label="Ring with yellow pear-cut stone"></div>
      <div class="gallery__item item-earrings-ruby" role="img" aria-label="Silver earrings with red stones"></div>
      <div class="gallery__item item-ring-sapphire" role="img" aria-label="Ring with oval blue stone"></div>
      <div class="gallery__item item-ring-emerald" role="img" aria-label="Ring with green marquise stone and pink accents"></div>
    </div>

    <div class="story">
      <div class="brand-name brand-name--back">PLUM VEXA</div>
      <h2 class="story__title">HANDMADE TURKISH<br>OTTOMAN-STYLE JEWELRY</h2>
      <p class="story__text">Plum Vexa was founded to bring traditional handcrafted Turkish jewelry to a wider audience of interest through our boutique-style Turkish jewelry store online. You will love the premium quality of our uniquely handcrafted products from Turkey.</p>
      <p class="story__web">WWW.PLUMVEXA.COM</p>
    </div>
  </section>

</body>
</html>
```